Design a 1-page brochure with our "The Harborline Pathway" illustrated.

i have included my logo, an outline of the text and name of each step, and a quick sketch of generally how i would like the image to look. But please make it look sexy.

Each step should include the subtext as shown on the pdf attached. i.e. The first part of the image (far left) is "Problems", under that should list : 1. Poor Expectations; 2. Poor Communication... and so on for all the steps included.

I have also included a previous brochure that shows our branding and style.

Target Market(s)

Restaurant, Retail, Commercial

Industry/Entity Type

Construction Management

Font styles to use
Sans Serif

Colors
EB3D1F
EC4F4E
F09395
F8D3D4
FCEDEE

Requirements
Must have
• Our logo. Title of graphic: The Harborline Pathway, our website and IG. www.brevanbuildco.example. @brevanbuildco

```html
<!DOCTYPE html>
<html lang="en">
<head>
<meta charset="utf-8">
<title>The Harborline Pathway – Brevan Build Co</title>
<link rel="stylesheet" href="https://fonts.googleapis.com/css2?family=Montserrat:wght@400;600;800&family=Source+Sans+3:wght@400;600&display=swap">
<style>
  :root {
    --backdrop: #e9e9eb;
    --paper: #ffffff;
    --ink: #231f20;
    --red: #e21f26;
    --red-orange: #eb3d1f;
    --rose: #f09395;
    --blush: #f8d3d4;
    --mist: #fcedee;
    --rule-grey: #ececec;
  }
  html, body {
    margin: 0;
    width: 1200px;
    height: 1000px;
    overflow: hidden;
    background: var(--backdrop);
  }
  .brochure {
    position: absolute;
    left: 0;
    top: 76px;
    width: 1200px;
    height: 848px;
    background: var(--paper);
  }
  .brochure svg { display: block; width: 100%; height: 100%; }
  .brand-name { font-family: "Montserrat", sans-serif; font-weight: 800; font-size: 15px; fill: var(--ink); letter-spacing: .2px; }
  .title { font-family: "Montserrat", sans-serif; font-size: 29px; letter-spacing: 9px; fill: var(--ink); font-weight: 600; }
  .title .title-lead { fill: var(--red); font-weight: 400; }
  .section-heading { font-family: "Source Sans 3", sans-serif; font-weight: 600; font-size: 16px; fill: var(--ink); }
  .list { font-family: "Source Sans 3", sans-serif; font-size: 13.5px; fill: var(--ink); }
  .step-name { font-family: "Source Sans 3", sans-serif; font-weight: 600; font-size: 15px; fill: var(--ink); }
  .step-item { font-family: "Source Sans 3", sans-serif; font-size: 12.5px; fill: var(--ink); }
  .contact { font-family: "Source Sans 3", sans-serif; font-size: 15px; fill: var(--ink); }
  .divider { stroke: var(--rule-grey); stroke-width: 1.5; }
  .step-box { fill: var(--paper); stroke: var(--red); stroke-width: 4; }
  .step-band { fill: var(--red); }
  .step-base { stroke: var(--ink); stroke-width: 5; }
  .connector { stroke: var(--red); stroke-width: 1.5; fill: none; }
  .connector-accent { stroke: var(--red-orange); stroke-width: 1.5; fill: none; }
</style>
</head>
<body>
<main class="brochure">
  <svg viewBox="0 0 1108 783" xmlns="http://www.w3.org/2000/svg" aria-label="The Harborline Pathway brochure">
    <defs>
      <linearGradient id="accent-fade-tr" x1="0" y1="1" x2="1" y2="0">
        <stop offset="0" stop-color="#ffffff"/>
        <stop offset="1" stop-color="#f09395"/>
      </linearGradient>
      <linearGradient id="accent-fade-bl" x1="1" y1="0" x2="0" y2="1">
        <stop offset="0" stop-color="#ffffff"/>
        <stop offset="1" stop-color="#f8d3d4"/>
      </linearGradient>
      <linearGradient id="accent-fade-bm" x1="0" y1="0" x2="0" y2="1">
        <stop offset="0" stop-color="#ffffff"/>
        <stop offset="1" stop-color="#fcedee"/>
      </linearGradient>
    </defs>

    <rect role="img" aria-label="Decorative cluster of red and maroon geometric shapes" x="820" y="0" width="288" height="130" fill="url(#accent-fade-tr)"/>
    <rect role="img" aria-label="Decorative cluster of grey and red geometric shapes" x="0" y="560" width="290" height="223" fill="url(#accent-fade-bl)"/>
    <rect role="img" aria-label="Decorative row of red and maroon geometric shapes" x="290" y="660" width="380" height="123" fill="url(#accent-fade-bm)"/>

    <line class="divider" x1="284" y1="37" x2="284" y2="230"/>

    <g class="brand">
      <rect x="127" y="50" width="60" height="60" fill="var(--red)"/>
      <text class="brand-name" x="157" y="206" text-anchor="middle">BREVAN BUILD CO</text>
    </g>

    <text class="title" x="316" y="114"><tspan class="title-lead">THE </tspan>HARBORLINE</text>
    <text class="title" x="316" y="154">PATHWAY</text>

    <g class="problems">
      <text class="section-heading" x="59" y="344">COMMON PROBLEMS</text>
      <text class="list" x="59" y="364">a.&#160;&#160;Changing or poor expectations</text>
      <text class="list" x="59" y="383">b.&#160;&#160;Poor Communication</text>
      <text class="list" x="59" y="402">c.&#160;&#160;No Journey To Success</text>
      <text class="list" x="59" y="421">d.&#160;&#160;No Trust</text>
      <text class="list" x="59" y="440">e.&#160;&#160;No Accountability</text>
      <polyline class="connector" points="236,338 300,338 300,360"/>
    </g>

    <g class="possibility">
      <text class="section-heading" x="817" y="205">POSSIBILITY</text>
      <g class="list">
        <text x="817" y="230">a.</text><text x="836" y="230">Project Synergy</text>
        <text x="817" y="249">b.</text><text x="836" y="249">Excellent Communication where</text>
        <text x="836" y="268">Budget and Schedule are visible</text>
        <text x="836" y="287">and approved.</text>
        <text x="817" y="306">c.</text><text x="836" y="306">Clear project visibility where</text>
        <text x="836" y="325">everyone understands how we get</text>
        <text x="836" y="344">to a successful end.</text>
        <text x="817" y="363">d.</text><text x="836" y="363">Everyone involved is proud of the</text>
        <text x="836" y="382">final product.</text>
      </g>
      <polyline class="connector-accent" points="812,197 774,197 774,248"/>
    </g>

    <g class="pathway">
      <g class="step step-organize">
        <rect class="step-box" x="306" y="350" width="108" height="222"/>
        <rect class="step-band" x="306" y="350" width="108" height="36"/>
        <line class="step-base" x1="300" y1="582" x2="420" y2="582"/>
        <text class="step-name" transform="translate(336,560) rotate(-90)">ORGANIZE</text>
        <text class="step-item" transform="translate(354,560) rotate(-90)">a. Develop Project Plan</text>
        <text class="step-item" transform="translate(372,560) rotate(-90)">b. Develop Schedule</text>
        <text class="step-item" transform="translate(390,560) rotate(-90)">c. Develop Budget</text>
      </g>

      <g class="step step-execute">
        <rect class="step-box" x="428" y="316" width="108" height="256"/>
        <rect class="step-band" x="428" y="316" width="108" height="36"/>
        <line class="step-base" x1="422" y1="582" x2="542" y2="582"/>
        <text class="step-name" transform="translate(476,560) rotate(-90)">EXECUTE</text>
        <text class="step-item" transform="translate(492,560) rotate(-90)">a. Project Start</text>
      </g>

      <g class="step step-manage">
        <rect class="step-box" x="550" y="282" width="108" height="290"/>
        <rect class="step-band" x="550" y="282" width="108" height="36"/>
        <line class="step-base" x1="544" y1="582" x2="664" y2="582"/>
        <text class="step-name" transform="translate(580,560) rotate(-90)">MANAGE</text>
        <text class="step-item" transform="translate(597,560) rotate(-90)">a. O.O.D.A</text>
        <text class="step-item" transform="translate(615,560) rotate(-90)">b. Shared Consciousness Meetings</text>
        <text class="step-item" transform="translate(633,560) rotate(-90)">c. Pressurized Collaboration</text>
      </g>

      <g class="step step-complete">
        <rect class="step-box" x="672" y="248" width="108" height="324"/>
        <rect class="step-band" x="672" y="248" width="108" height="36"/>
        <line class="step-base" x1="666" y1="582" x2="786" y2="582"/>
        <text class="step-name" transform="translate(718,560) rotate(-90)">COMPLETE</text>
        <text class="step-item" transform="translate(734,560) rotate(-90)">a. Project Closeout</text>
      </g>
    </g>

    <g class="contact-line">
      <circle cx="699" cy="735" r="8" fill="var(--red)"/>
      <text class="contact" x="714" y="740">www.brevanbuildco.example</text>
      <circle cx="916" cy="735" r="8" fill="var(--red)"/>
      <text class="contact" x="930" y="740">@brevanbuildco</text>
    </g>
  </svg>
</main>
</body>
</html>
```